Tenth Annual Silverwave Ivory Costume Soiree to Benefit Harborlight Capital Circle Trust

Date: 2 February 2024
Location: The Corvane Palmridge Coralbay Shore Resort & Spa
Time: Doors open 5:00pm
Attire: White Elegance (a variety of masks will be available at the extravaganza)

Target Market(s)

Early to mid career men and women (aged 25-40)

Industry/Entity Type

Financial Services / Asset Management

Font styles to use
Serif

Colors
0054AA
0677BA
7BADD7
CADEEF
E8F1F8
00AB8E
00BBA5
67D7C9
C6EFE9
E9F9F6
59FF00
82FF00
B8FF75
E3FFCB
F4FFEA

Requirements
Must have
• Masquerade images. The event is being held on the beach in the Caribbean.

```html
<!DOCTYPE html>
<html lang="en">
<head>
<meta charset="utf-8">
<title>Tenth Annual Silverwave Ivory Costume Soiree</title>
<link href="https://fonts.googleapis.com/css2?family=Montserrat:wght@400;500;700&family=Sacramento&family=Damion&display=swap" rel="stylesheet">
<style>
  :root {
    --stage: #d6eff4;
    --paper: #ffffff;
    --navy: #24248f;
    --green: #7cc242;
    --rule: #4a4a9a;
    --ink-soft: #3b3b4a;
    --sky: #bfe3f2;
    --sea: #2cb4c4;
    --sea-deep: #168fa6;
    --sand: #e6d6c0;
  }
  * { margin: 0; padding: 0; box-sizing: border-box; }
  html, body { width: 1200px; height: 800px; overflow: hidden; }
  body {
    background: var(--stage);
    font-family: "Montserrat", Arial, sans-serif;
    position: relative;
  }
  .flyer {
    position: absolute;
    left: 324px;
    top: 10px;
    width: 552px;
    height: 780px;
    background: var(--paper);
    overflow: hidden;
  }
  .hero {
    position: absolute;
    left: 0; top: 0;
    width: 552px;
    height: 525px;
    background:
      linear-gradient(to bottom, rgba(255,255,255,0) 0%, rgba(255,255,255,0) 82%, #fff 100%),
      linear-gradient(to bottom, var(--sky) 0%, #d7edf4 10%, var(--sea-deep) 20%, var(--sea) 34%, #bfe6ea 46%, var(--sand) 52%, #eadfce 80%, #f3ede4 100%);
  }
  .brand {
    position: absolute;
    left: 0; right: 0;
    top: 490px;
    display: flex;
    justify-content: center;
    align-items: center;
    gap: 10px;
  }
  .brand-dot {
    width: 18px; height: 18px;
    border-radius: 50%;
    background: var(--green);
  }
  .brand-name {
    font-weight: 700;
    font-size: 19px;
    color: var(--navy);
    letter-spacing: -0.2px;
  }
  .event-kicker {
    position: absolute;
    left: 0; right: 0; top: 548px;
    text-align: center;
    font-family: "Sacramento", cursive;
    font-size: 32px;
    color: var(--green);
    line-height: 1;
  }
  .event-title {
    position: absolute;
    left: 0; right: 0; top: 578px;
    text-align: center;
    font-family: "Damion", cursive;
    font-size: 44px;
    color: var(--navy);
    line-height: 1;
    letter-spacing: 0.3px;
  }
  .details {
    position: absolute;
    left: 61px; top: 644px;
    width: 430px; height: 67px;
    border-top: 1px solid var(--rule);
    border-bottom: 1px solid var(--rule);
    display: flex;
    padding-top: 9px;
  }
  .detail {
    display: flex;
    gap: 5px;
    height: 46px;
  }
  .detail + .detail {
    border-left: 1px solid var(--rule);
    margin-left: 9px;
    padding-left: 9px;
  }
  .detail-date { width: 84px; }
  .detail-time { width: 97px; }
  .detail-place { flex: 1; }
  .detail-icon { width: 13px; height: 13px; flex: none; margin-top: 1px; }
  .detail-label {
    font-size: 9.5px; font-weight: 700; color: var(--green);
    line-height: 12px;
  }
  .detail-value {
    margin-top: 5px;
    font-size: 10.5px; font-weight: 700; color: var(--navy);
    line-height: 15px;
  }
  .attire {
    position: absolute;
    left: 0; right: 0; top: 720px;
    text-align: center;
    font-size: 10.5px; font-weight: 700; color: var(--navy);
  }
  .attire-label { color: var(--green); }
  .attire-note {
    position: absolute;
    left: 0; right: 0; top: 737px;
    text-align: center;
    font-size: 8px; font-weight: 500; color: var(--ink-soft);
  }
</style>
</head>
<body>
  <main class="flyer">
    <div class="hero" role="img" aria-label="White and gold Venetian masquerade mask resting on Caribbean beach sand with white flowers and turquoise sea behind"></div>

    <div class="brand">
      <span class="brand-dot"></span>
      <span class="brand-name">Harborlight Capital Circle Trust</span>
    </div>

    <p class="event-kicker">Tenth Annual Silverwave</p>
    <h1 class="event-title">Ivory Costume Soiree</h1>

    <section class="details">
      <div class="detail detail-date">
        <svg class="detail-icon" viewBox="0 0 14 14" fill="none" stroke="#24248f" stroke-width="1">
          <rect x="1" y="2.5" width="12" height="10.5" rx="1"/>
          <line x1="1" y1="5.5" x2="13" y2="5.5"/>
          <line x1="4" y1="1" x2="4" y2="4"/><line x1="10" y1="1" x2="10" y2="4"/>
          <g fill="#24248f" stroke="none">
            <rect x="3" y="7" width="1.5" height="1.5"/><rect x="6.2" y="7" width="1.5" height="1.5"/><rect x="9.4" y="7" width="1.5" height="1.5"/>
            <rect x="3" y="10" width="1.5" height="1.5"/><rect x="6.2" y="10" width="1.5" height="1.5"/><rect x="9.4" y="10" width="1.5" height="1.5"/>
          </g>
        </svg>
        <div>
          <div class="detail-label">Date:</div>
          <div class="detail-value">2 February<br>2024</div>
        </div>
      </div>
      <div class="detail detail-time">
        <svg class="detail-icon" viewBox="0 0 14 14" fill="none" stroke="#24248f" stroke-width="1">
          <circle cx="7" cy="7" r="6"/>
          <polyline points="7,3.5 7,7 9.5,8.5"/>
        </svg>
        <div>
          <div class="detail-label">Time:</div>
          <div class="detail-value">Doors open<br>5:00pm</div>
        </div>
      </div>
      <div class="detail detail-place">
        <svg class="detail-icon" viewBox="0 0 14 14" fill="none" stroke="#24248f" stroke-width="1">
          <path d="M7 13 C4 9.5 2.5 7.5 2.5 5.5 A4.5 4.5 0 0 1 11.5 5.5 C11.5 7.5 10 9.5 7 13 Z"/>
          <circle cx="7" cy="5.5" r="1.6"/>
        </svg>
        <div>
          <div class="detail-label">Location:</div>
          <div class="detail-value">The Corvane Palmridge Coralbay<br>Shore Resort &amp; Spa</div>
        </div>
      </div>
    </section>

    <p class="attire"><span class="attire-label">Attire:</span> White Elegance</p>
    <p class="attire-note">(a variety of masks will be available at the extravaganza)</p>
  </main>
</body>
</html>
```